Etiketten für Weinbaubetrieb
Recht herzlichen Dank für die rasche Umsetzung und die punktgenaue Umsetzung von diversen Wünschen. Das Design hat uns schwer begeistert, wir hoffen dass dieses genauso gut ankommt bei unseren Kunden wie bei uns.
Zielgruppe
Weinbaubetrieb
Aufgabenstellung
Wollen ein neues Flaschen-Etikett für unsere Wein Magnumflaschen kreieren (Limitierte Stückzahl), Hintergrund soll Schwarz sein, Stil: Schlicht und Edel, ca 9,5 x 9,5 cm / Schwarz/weiß max. silber und Gold (Logo muss nicht unbedingt ersichtlich sein)
Bezeichnung: quiet harbor;
limited edion weingut brandt
Angefügt sind unsere bisherige Etikette weißwein: DAC.jpg u. Rotwein: roesler.jpg
bzw. in welche Richtung es gehen soll: Magnnum.pdf

```html
<!DOCTYPE html>
<html lang="de">
<head>
<meta charset="utf-8">
<title>quiet harbor – Limited Edition Etikett</title>
<link rel="stylesheet" href="https://fonts.googleapis.com/css2?family=Abril+Fatface&family=Sacramento&family=Mrs+Saint+Delafield&display=swap">
<style>
  :root {
    --stage: #161618;
    --label-black: #07080b;
    --gold: #b98a45;
    --gold-light: #d2a560;
    --silver: #c9ccd1;
  }
  * { box-sizing: border-box; margin: 0; padding: 0; }
  html, body {
    width: 1200px;
    height: 1200px;
    overflow: hidden;
    background: var(--stage);
  }
  .canvas {
    position: relative;
    width: 1200px;
    height: 1200px;
    display: flex;
    align-items: center;
    justify-content: center;
  }
  .label {
    position: relative;
    width: 900px;
    height: 900px;
    background: var(--label-black);
    box-shadow: 0 0 0 1px #202226;
    overflow: hidden;
  }
  .label__title {
    position: absolute;
    left: 130px;
    top: 150px;
    width: 640px;
    display: flex;
    flex-direction: column;
    font-weight: 400;
  }
  .title__main {
    display: block;
    font-family: "Abril Fatface", "Didot", serif;
    font-size: 210px;
    line-height: 1.3;
    letter-spacing: 0;
    color: var(--gold);
    text-align: right;
  }
  .title__sub {
    display: block;
    margin-top: -6px;
    padding-left: 40px;
    font-family: "Sacramento", cursive;
    font-size: 88px;
    line-height: 1.1;
    color: var(--gold-light);
    text-align: left;
  }
  .label__edition {
    position: absolute;
    left: 110px;
    top: 600px;
    width: 680px;
    font-family: "Mrs Saint Delafield", cursive;
    font-size: 82px;
    line-height: 1.15;
    color: var(--silver);
    text-align: center;
  }
  .label__edition span { display: block; }
</style>
</head>
<body>
  <main class="canvas">
    <section class="label" aria-label="Flaschenetikett quiet harbor, Limited Edition">
      <h1 class="label__title">
        <span class="title__main">quiet</span>
        <span class="title__sub">harbor</span>
      </h1>
      <p class="label__edition">
        <span>Limited edition</span>
        <span>weingut brandt</span>
      </p>
    </section>
  </main>
</body>
</html>
```